I need a better looking dashboard for my web application

I have a very table heavy web page that I would like to add a design touch to it. I have the logo and primary colors picked out, I just need some help in adding visual appeal the page. I would also like to add a couple of button to the page as shortcuts. Every spot that has a + sign could have a button added. I would also like to add another graph (the data will be in the uploaded files. Please feel free to ask any questions :-)

```html
<!DOCTYPE html>
<html lang="en">
<head>
<meta charset="utf-8">
<title>ShiftCover Dashboard</title>
<link href="https://fonts.googleapis.com/css2?family=Poppins:wght@400;500;600;700&display=swap" rel="stylesheet">
<style>
:root{
  --stage:#1e1b2f;
  --stage-2:#262238;
  --purple:#6a50bd;
  --purple-soft:#ece7fb;
  --purple-light:#d8cff6;
  --cyan:#2bb3d6;
  --ink:#1c1a28;
  --muted:#8a8799;
  --line:#ecebf1;
  --main-bg:#f2f1f7;
  --white:#ffffff;
  --green:#22a559;
  --green-bg:#e2f6e9;
  --orange:#ef8a23;
  --orange-bg:#fdecd9;
  --red:#e5484d;
  --red-bg:#fde4e4;
  --grey-bg:#ececf0;
  --annot:#d4d1e2;
}
*{box-sizing:border-box;margin:0;padding:0}
html,body{width:1200px;height:870px;overflow:hidden}
body{font-family:'Poppins',sans-serif;background:radial-gradient(ellipse at 50% 30%,var(--stage-2),var(--stage) 70%);color:var(--ink);position:relative}
.abs{position:absolute}

.brand-top{position:absolute;top:48px;left:0;width:1200px;display:flex;justify-content:center;align-items:center;gap:10px}
.brand-top .dot{width:18px;height:18px;border-radius:50%;background:var(--purple)}
.brand-top .name{font-size:30px;font-weight:500;color:#8b70e2;letter-spacing:-.3px}

.frame{position:absolute;left:143px;top:122px;width:914px;height:592px;border-radius:14px;overflow:hidden;background:var(--main-bg)}

/* sidebar */
.sidebar{position:absolute;left:0;top:0;width:152px;height:100%;background:linear-gradient(180deg,#4c3b7e 0%,#3a2d63 55%,#2d2349 100%);color:#fff}
.side-brand{position:absolute;left:29px;top:20px;display:flex;align-items:center;gap:6px}
.side-brand .dot{width:10px;height:10px;border-radius:50%;background:#fff}
.side-brand .name{font-size:14px;font-weight:500}
.create-btn{position:absolute;left:15px;top:71px;width:122px;height:32px;border-radius:16px;background:#fff;display:flex;align-items:center;gap:9px;padding-left:15px;color:var(--purple);font-size:8.5px;font-weight:600}
.create-btn .plus{width:11px;height:12px;border-radius:2px;background:var(--purple);color:#fff;font-size:9px;line-height:12px;text-align:center}
.nav{position:absolute;left:15px;top:128px;width:122px}
.nav-item{height:31px;margin-bottom:1px;display:flex;align-items:center;padding-left:11px;gap:12px;font-size:7.5px;font-weight:500;border-radius:5px;position:relative}
.nav-item.active{background:#6a55b3}
.nav-item svg{width:11px;height:11px}
.nav-item .chev{position:absolute;right:9px;font-size:8px;opacity:.8}
.nav-item .badge{position:absolute;right:6px;width:12px;height:12px;border-radius:50%;background:#2a9df4;font-size:6px;text-align:center;line-height:12px}
.logout{position:absolute;left:15px;top:512px;width:122px;height:31px;border-radius:6px;background:#2a2042;display:flex;align-items:center;gap:10px;padding-left:11px;font-size:7.5px;color:#ff6d7a}
.copyright{position:absolute;left:15px;top:557px;width:125px;font-size:6px;line-height:9.5px;color:#c9c2dd}

/* main */
.main{position:absolute;left:152px;top:0;width:762px;height:100%}
.topbar{position:absolute;left:0;top:0;width:100%;height:46px;background:#fff;border-bottom:1px solid var(--line)}
.page-title{position:absolute;left:26px;top:12px;font-size:15px;font-weight:600}
.tabs{position:absolute;left:310px;top:11px;width:146px;height:23px;background:#e6e5ec;border-radius:5px;padding:2px;display:flex}
.tab{flex:1;font-size:7.5px;font-weight:500;color:var(--muted);display:flex;align-items:center;justify-content:center;border-radius:4px}
.tab.on{background:#fff;color:var(--purple);font-weight:600}
.bell{position:absolute;left:613px;top:15px}
.bell .count{position:absolute;left:6px;top:-5px;width:10px;height:10px;border-radius:50%;background:#2a9df4;color:#fff;font-size:5.5px;text-align:center;line-height:10px;border:1px solid #fff}
.user{position:absolute;left:651px;top:12px;display:flex;align-items:center;gap:6px}
.user .pic{width:20px;height:20px;border-radius:50%;background:linear-gradient(135deg,#7c8aa8,#3e4659)}
.user .n{font-size:7.5px;font-weight:600;line-height:10px}
.user .r{font-size:6px;color:var(--muted)}
.user .caret{font-size:6px;color:var(--muted);margin-left:10px}

.section-title{position:absolute;left:26px;top:61px;font-size:11px;font-weight:600}
.updated{position:absolute;left:468px;top:66px;font-size:6px;color:var(--muted);display:flex;gap:4px;align-items:center}

.stat{position:absolute;top:82px;width:120px;height:66px;border-radius:7px;background:#fff;padding:10px 10px;overflow:hidden}
.stat .num{font-size:12.5px;font-weight:600}
.stat .lbl{font-size:7px;color:var(--muted);margin-top:3px}
.stat .trend{font-size:5.5px;margin-top:9px;display:flex;align-items:center;gap:5px}
.stat .trend .up{color:var(--green)}
.stat .trend .down{color:var(--red)}
.stat .ico{position:absolute;right:10px;top:10px;width:15px;height:15px;border-radius:4px;display:flex;align-items:center;justify-content:center}
.stat.s1{background:linear-gradient(115deg,#fff 35%,#f7e3f6 75%,#eed9f5)}
.stat.s1 .ico{background:#b451d6}
.stat.s2{background:linear-gradient(115deg,#fff 35%,#e0f3f7 75%,#cdeef4)}
.stat.s2 .ico{background:var(--cyan)}
.stat.s3{background:linear-gradient(115deg,#fff 35%,#e6ebfb 75%,#e4ddf7)}
.stat.s3 .ico{background:#4f7ae0}
.stat.s4{background:linear-gradient(115deg,#fff 35%,#efe6fb 75%,#e6d6f7)}
.stat.s4 .ico{background:#6a50bd}

.panel{position:absolute;background:#fff;border-radius:7px;overflow:hidden}
.panel-head{height:35px;display:flex;align-items:center;padding:0 10px;gap:6px;position:relative}
.panel-head h2{font-size:9.5px;font-weight:600}
.search{position:absolute;height:19px;border:1px solid #e2e1e8;border-radius:4px;font-size:6px;color:#a09eae;display:flex;align-items:center;padding-left:7px}
.search svg{position:absolute;right:7px;top:5px}
.add-link{position:absolute;right:26px;top:13px;font-size:8px;font-weight:600;color:var(--purple);display:flex;gap:5px;align-items:center}

.cols{display:flex;align-items:center;background:#f5f5f8;font-size:5.5px;font-weight:600;color:#3c3a48;letter-spacing:.2px;padding-left:10px}
.cols small{display:block;font-weight:400;color:var(--muted);font-size:5.5px}
.row{height:28px;display:flex;align-items:center;border-bottom:1px solid var(--line);font-size:6.5px;padding-left:10px;position:relative}
.row.hover{background:#f7f5fc}
.cell{white-space:nowrap;overflow:hidden;flex-shrink:0;display:flex;align-items:center;gap:7px}
.cell.strong{font-weight:600}
.avatar{width:13px;height:13px;border-radius:50%;flex-shrink:0}
.avatar.blank{background:#e3e2ea}
.pill{font-size:5.3px;font-weight:600;padding:3px 0;width:46px;text-align:center;border-radius:3px;letter-spacing:.2px}
.pill.assigned{background:var(--grey-bg);color:#3a3848}
.pill.available{background:var(--green-bg);color:var(--green)}
.pill.pending{background:var(--orange-bg);color:var(--orange)}
.pill.approved{background:var(--green-bg);color:var(--green)}
.pill.cancelled{background:var(--red-bg);color:var(--red)}
.time{display:flex;align-items:center}
.time .date{width:54px}
.time .dur{display:flex;gap:4px;align-items:center}
.faded{color:#b9b7c4}
.row-actions{position:absolute;display:flex;gap:9px}
.act{width:19px;height:19px;border-radius:50%;display:flex;align-items:center;justify-content:center;box-shadow:0 1px 3px rgba(60,40,120,.18)}
.act.del{background:#fff}
.act.view{background:#fff}
.act.edit{background:var(--purple)}
.scroll{position:absolute;width:3px;border-radius:2px;background:#c9c8d2}

.card{position:absolute;left:549px;width:188px;background:#fff;border-radius:7px;overflow:hidden}
.card h3{position:absolute;left:30px;font-size:9.5px;font-weight:600}
.legend-row{position:absolute;left:10px;width:168px;font-size:6.5px}
.legend-row .bar{position:absolute;left:0;top:11px;width:89px;height:2px;background:#eeedf3;border-radius:2px}
.legend-row .bar i{display:block;height:100%;border-radius:2px}
.legend-row .v{position:absolute;left:105px;top:9px;font-weight:600}
.legend-row .v span{font-weight:400;color:var(--muted)}
.legend-row .p{position:absolute;right:0;top:9px;font-weight:600}

.profile{position:absolute;left:10px;width:168px}
.profile .face{position:absolute;left:0;top:0;width:30px;height:30px;border-radius:50%}
.profile .nm{position:absolute;left:39px;top:-3px;font-size:7px;font-weight:600}
.profile .vf{position:absolute;left:39px;top:7px;font-size:6px;color:var(--muted);display:flex;gap:3px;align-items:center}
.profile .btn{position:absolute;top:18px;width:62px;height:14px;border-radius:3px;font-size:5.5px;font-weight:600;display:flex;align-items:center;justify-content:center;gap:3px}
.btn.approve{left:39px;border:1px solid var(--purple);color:var(--purple)}
.btn.decline{left:106px;border:1px solid var(--red);color:var(--red)}
.profile .sep{position:absolute;left:0;top:-9px;width:168px;height:1px;background:var(--line)}

.annot{position:absolute;top:759px;display:flex;align-items:center;gap:5px;font-size:9.5px;color:var(--annot)}
.annot .tag{background:var(--purple-light);color:#3b2a6e;border-radius:8px;padding:1px 8px;font-size:8.5px;font-weight:500}
.connectors{position:absolute;left:0;top:0;width:1200px;height:870px;pointer-events:none}
</style>
</head>
<body>
<svg width="0" height="0" style="position:absolute">
  <defs>
    <symbol id="clock" viewBox="0 0 12 12"><circle cx="6" cy="6" r="5" fill="none" stroke="#555" stroke-width="1.2"/><path d="M6 3.2V6l2 1.2" fill="none" stroke="#555" stroke-width="1.2" stroke-linecap="round"/></symbol>
    <symbol id="search" viewBox="0 0 12 12"><circle cx="5" cy="5" r="3.8" fill="none" stroke="#6a50bd" stroke-width="1.6"/><path d="M8 8l3 3" stroke="#6a50bd" stroke-width="1.6" stroke-linecap="round"/></symbol>
    <symbol id="arrow-down" viewBox="0 0 10 10"><circle cx="5" cy="5" r="4.4" fill="none" stroke="#9a98a8" stroke-width=".8"/><path d="M5 2.8v4.2M3.3 5.4L5 7l1.7-1.6" fill="none" stroke="#6a50bd" stroke-width=".9"/></symbol>
    <symbol id="pencil" viewBox="0 0 12 12"><path d="M2 10l.6-2.6L8 2l2 2-5.4 5.4z" fill="#fff"/></symbol>
    <symbol id="check-badge" viewBox="0 0 10 10"><circle cx="5" cy="5" r="5" fill="#6a50bd"/><path d="M2.8 5.1l1.5 1.5 2.9-3" fill="none" stroke="#fff" stroke-width="1.1"/></symbol>
    <symbol id="ban" viewBox="0 0 10 10"><circle cx="5" cy="5" r="4" fill="none" stroke="#e5484d" stroke-width="1"/><path d="M2.3 7.7l5.4-5.4" stroke="#e5484d" stroke-width="1"/></symbol>
    <symbol id="user" viewBox="0 0 12 12"><circle cx="6" cy="4.2" r="2.2" fill="#fff"/><path d="M2 10.5c.6-2.3 2.2-3.5 4-3.5s3.4 1.2 4 3.5z" fill="#fff"/></symbol>
  </defs>
</svg>

<div class="brand-top"><span class="dot"></span><span class="name">ShiftCover</span></div>

<div class="frame">
  <aside class="sidebar">
    <div class="side-brand"><span class="dot"></span><span class="name">ShiftCover</span></div>
    <div class="create-btn"><span class="plus">+</span>Create absence</div>
    <nav class="nav">
      <div class="nav-item active"><svg viewBox="0 0 12 12"><rect x="0" y="0" width="12" height="5" rx="1" fill="#fff"/><rect x="0" y="7" width="5" height="5" rx="1" fill="#fff"/><rect x="7" y="7" width="5" height="5" rx="1" fill="#fff"/></svg>Dashboard</div>
      <div class="nav-item"><svg viewBox="0 0 12 12"><circle cx="6" cy="6" r="5.5" fill="#fff"/><circle cx="4" cy="5" r="1.2" fill="#3a2d63"/><circle cx="8" cy="5" r="1.2" fill="#3a2d63"/><path d="M3.5 8.5h5" stroke="#3a2d63"/></svg>Regular Staff<span class="chev">›</span></div>
      <div class="nav-item"><svg viewBox="0 0 12 12"><path d="M6 1C3 1 .8 3 .8 5.4c0 1.3.6 2.4 1.6 3.2L2 11l2.7-1.4c.4.1.9.2 1.3.2 3 0 5.2-2 5.2-4.4S9 1 6 1z" fill="#fff"/></svg>Messages<span class="badge">8</span></div>
      <div class="nav-item"><svg viewBox="0 0 12 12"><rect x=".7" y="1.5" width="10.6" height="7.5" rx="1" fill="none" stroke="#fff" stroke-width="1.2"/><path d="M5 3.8v3l2.5-1.5z" fill="#fff"/><path d="M3 11h6" stroke="#fff" stroke-width="1.2"/></svg>Demo Outbox</div>
      <div class="nav-item"><svg viewBox="0 0 12 12"><circle cx="6" cy="4.5" r="3.5" fill="none" stroke="#fff" stroke-width="1.2"/><circle cx="6" cy="4.5" r="1.2" fill="#fff"/><path d="M3 8l-1.5 3.5h9L9 8" fill="none" stroke="#fff" stroke-width="1.2"/></svg>Admin Location<span class="chev">›</span></div>
      <div class="nav-item"><svg viewBox="0 0 12 12"><circle cx="6" cy="6" r="3.6" fill="none" stroke="#fff" stroke-width="2.4" stroke-dasharray="1.8 1"/><circle cx="6" cy="6" r="1.3" fill="#fff"/></svg>Regular Services</div>
    </nav>
    <div class="logout"><svg width="11" height="11" viewBox="0 0 12 12"><path d="M7 1.5h3v9H7M1 6h6M4.5 3.5L7 6 4.5 8.5" fill="none" stroke="#ff6d7a" stroke-width="1.2"/></svg>Log out</div>
    <p class="copyright">Copyright © 2025. Northbeam Ed Systems. All Rights Reserved. (v0.8.4)</p>
  </aside>

  <main class="main">
    <header class="topbar">
      <h1 class="page-title">Dashboard</h1>
      <div class="tabs"><span class="tab on">Overview</span><span class="tab">Calendar</span></div>
      <div class="bell"><svg width="11" height="12" viewBox="0 0 12 13"><path d="M6 1a3.6 3.6 0 00-3.6 3.6v3L1 9.5h10L9.6 7.6v-3A3.6 3.6 0 006 1z" fill="#4a4858"/><circle cx="6" cy="11.3" r="1.3" fill="#4a4858"/></svg><span class="count">4</span></div>
      <div class="user"><span class="pic" role="img" aria-label="User profile photo"></span><div><div class="n">Daniel R.</div><div class="r">Manager</div></div><span class="caret">▼</span></div>
    </header>

    <h2 class="section-title">Today’s summary</h2>
    <div class="updated"><svg width="7" height="7" viewBox="0 0 10 10"><path d="M8.5 5A3.5 3.5 0 115 1.5h1.5" fill="none" stroke="#6a50bd" stroke-width="1.1"/><path d="M5.5 0l1.6 1.5L5.5 3" fill="none" stroke="#6a50bd" stroke-width="1"/></svg>Last updated: 2 Jan 2025 at 10:48 AM</div>

    <div class="stat s1" style="left:26px"><div class="num">4</div><div class="lbl">Unfilled</div><div class="trend"><span class="up">↑</span><span class="up">1.87%</span></div><span class="ico"><svg width="8" height="8"><use href="#user"/></svg></span></div>
    <div class="stat s2" style="left:153px"><div class="num">13</div><div class="lbl">Filled</div><div class="trend"><span class="down">↓</span><span class="down">1.90%</span></div><span class="ico"><svg width="8" height="8"><use href="#user"/></svg></span></div>
    <div class="stat s3" style="left:281px"><div class="num">29</div><div class="lbl">No sub needed</div><div class="trend"><span class="up">↑</span><span class="up">2.06%</span></div><span class="ico"><svg width="8" height="8"><use href="#user"/></svg></span></div>
    <div class="stat s4" style="left:409px"><div class="num">46</div><div class="lbl">Total</div><div class="trend"><span class="up">↑</span><span class="up">1.02%</span></div><span class="ico"><svg width="8" height="8"><use href="#user"/></svg></span></div>

    <!-- Manage openings -->
    <section class="panel" style="left:26px;top:161px;width:503px;height:213px">
      <div class="panel-head">
        <svg width="12" height="10" viewBox="0 0 14 11"><circle cx="4" cy="3" r="2.2" fill="#8c86a8"/><circle cx="10" cy="3" r="2.2" fill="#8c86a8"/><path d="M0 10c.4-2.5 2-3.6 4-3.6S7.6 7.5 8 10zM6 10c.4-2.5 2-3.6 4-3.6s3.6 1.1 4 3.6z" fill="#8c86a8"/></svg>
        <h2>Manage openings</h2>
        <div class="search" style="left:302px;top:8px;width:138px">Search staff, category<svg width="7" height="7"><use href="#search"/></svg></div>
        <div class="add-link"><svg width="10" height="8" viewBox="0 0 12 10"><circle cx="4.5" cy="3" r="2.2" fill="#6a50bd"/><path d="M.5 9.5c.4-2.3 2-3.3 4-3.3s3.6 1 4 3.3z" fill="#6a50bd"/><path d="M10 2v4M8 4h4" stroke="#6a50bd" stroke-width="1.2"/></svg>Add</div>
      </div>
      <div class="cols" style="height:24px">
        <span class="cell" style="width:105px">REGULAR STAFF <svg width="7" height="7"><use href="#arrow-down"/></svg></span>
        <span class="cell" style="width:67px">CATEGORY</span>
        <span class="cell" style="width:61px">STATUS <svg width="7" height="7"><use href="#arrow-down"/></svg></span>
        <span class="cell" style="width:99px">SUMMARY</span>
        <span class="cell" style="width:51px">LOCATION</span>
        <span class="cell">TIME SLOTS SUMMARY <svg width="7" height="7"><use href="#arrow-down"/></svg></span>
      </div>
      <div class="row"><span class="cell strong" style="width:105px"><span class="avatar blank"></span>Extra duty</span><span class="cell" style="width:67px">Food service</span><span class="cell" style="width:61px"><span class="pill assigned">ASSIGNED</span></span><span class="cell" style="width:99px">Immediate Need! This is a...</span><span class="cell" style="width:51px">LJE</span><span class="time"><span class="date">12/30 - 01/01</span><span class="dur"><svg width="7" height="7"><use href="#clock"/></svg>2h 30m</span></span></div>
      <div class="row"><span class="cell strong" style="width:105px"><span class="avatar" style="background:#d9b48a" role="img" aria-label="Staff photo"></span>Nora Whitfield</span><span class="cell" style="width:67px">Teacher</span><span class="cell" style="width:61px"><span class="pill available">AVAILABLE</span></span><span class="cell" style="width:99px">Immediate Need! Mathem...</span><span class="cell" style="width:51px">WDMS</span><span class="time"><span class="date">02/12 - 02/16</span><span class="dur"><svg width="7" height="7"><use href="#clock"/></svg>4h 30m</span></span></div>
      <div class="row hover"><span class="cell strong" style="width:105px"><span class="avatar" style="background:#5d5a66" role="img" aria-label="Staff photo"></span>Dario Kesler</span><span class="cell" style="width:67px">Bus Driver</span><span class="cell" style="width:61px"><span class="pill available">AVAILABLE</span></span><span class="cell" style="width:99px">Urgent Hiring! We are in ne...</span><span class="cell" style="width:51px">WDMS</span><span class="time"><span class="date">02/03 - 02/<span class="faded">07</span></span></span>
        <div class="row-actions" style="left:446px;top:4px"><span class="act del"><svg width="7" height="8" viewBox="0 0 10 11"><path d="M1 2.5h8M4 1h2M2 2.5l.6 7.5h4.8L8 2.5z" fill="#e5484d" stroke="#e5484d" stroke-width=".8"/></svg></span><span class="act edit"><svg width="8" height="8"><use href="#pencil"/></svg></span></div>
      </div>
      <div class="row"><span class="cell strong" style="width:105px"><span class="avatar blank"></span>Extra duty</span><span class="cell" style="width:67px">Custodian</span><span class="cell" style="width:61px"><span class="pill assigned">ASSIGNED</span></span><span class="cell" style="width:99px">Seeking sub for /couns...</span><span class="cell" style="width:51px">FMS</span><span class="time"><span class="date">01/06 - 01/10</span><span class="dur"><svg width="7" height="7"><use href="#clock"/></svg>3h 50m</span></span></div>
      <div class="row"><span class="cell strong" style="width:105px"><span class="avatar" style="background:#3a2e2a" role="img" aria-label="Staff photo"></span>Miles Brandt</span><span class="cell" style="width:67px">Teacher's Aide</span><span class="cell" style="width:61px"><span class="pill available">AVAILABLE</span></span><span class="cell" style="width:99px">Urgent Hiring! We are in ne...</span><span class="cell" style="width:51px">WDMS</span><span class="time"><span class="date">02/03 - 02/07</span><span class="dur"><svg width="7" height="7"><use href="#clock"/></svg>3h 45m</span></span></div>
      <div class="row"><span class="cell strong" style="width:105px"><span class="avatar blank"></span>Extra duty</span><span class="cell" style="width:67px">Custodian</span><span class="cell" style="width:61px"><span class="pill available">AVAILABLE</span></span><span class="cell" style="width:99px">Seeking sub for /couns...</span><span class="cell" style="width:51px">FMS</span><span class="time"><span class="date">01/06 - 01/10</span><span class="dur"><svg width="7" height="7"><use href="#clock"/></svg>3h 50m</span></span></div>
      <span class="scroll" style="left:496px;top:64px;height:45px"></span>
    </section>

    <!-- Leave requests -->
    <section class="panel" style="left:26px;top:387px;width:503px;height:230px">
      <div class="panel-head" style="height:36px">
        <svg width="9" height="11" viewBox="0 0 10 12"><path d="M1 0h6l3 3v9H1z" fill="#9e99b4"/><path d="M3 7h4M3 9h3" stroke="#fff" stroke-width=".9"/></svg>
        <h2>Regular Staffs Leave Requests</h2>
        <div class="search" style="left:353px;top:8px;width:139px">Search name, assignment<svg width="7" height="7"><use href="#search"/></svg></div>
      </div>
      <div class="cols" style="height:28px">
        <span class="cell" style="width:118px">FULL NAME <svg width="7" height="7"><use href="#arrow-down"/></svg></span>
        <span class="cell" style="width:80px;display:block">ASSIGNMENT<small>(OPENING)</small></span>
        <span class="cell" style="width:118px;display:block">PRE-ARRANGED SUB<small>(OPENING)</small></span>
        <span class="cell" style="width:67px">STATUS <svg width="7" height="7"><use href="#arrow-down"/></svg></span>
        <span class="cell">TIME SLOTS SUMMARY <svg width="7" height="7"><use href="#arrow-down"/></svg></span>
      </div>
      <div class="row"><span class="cell" style="width:118px"><span class="avatar" style="background:#dcb892" role="img" aria-label="Staff photo"></span>Leona Pratt</span><span class="cell" style="width:80px">Custodian</span><span class="cell" style="width:118px"><span class="avatar" style="background:#8a6a54" role="img" aria-label="Substitute photo"></span>Tessa Marlow</span><span class="cell" style="width:67px"><span class="pill pending">PENDING</span></span><span class="time"><span class="date">01/06 - 01/10</span><span class="dur"><svg width="7" height="7"><use href="#clock"/></svg>3h 50m</span></span></div>
      <div class="row hover"><span class="cell" style="width:118px"><span class="avatar" style="background:#5d5a66" role="img" aria-label="Staff photo"></span>Dario Kesler</span><span class="cell" style="width:80px">Bus Driver</span><span class="cell" style="width:118px"><span class="avatar" style="background:#6b5a4e" role="img" aria-label="Substitute photo"></span>Felix Ortand</span><span class="cell" style="width:67px"><span class="pill pending">PENDING</span></span><span class="time"><span class="date">02/03 - 02/<span class="faded">07</span></span></span>
        <div class="row-actions" style="left:446px;top:4px"><span class="act view"><svg width="9" height="7" viewBox="0 0 12 8"><path d="M.5 4C2 1.5 4 .5 6 .5s4 1 5.5 3.5C10 6.5 8 7.5 6 7.5S2 6.5.5 4z" fill="#6a50bd"/><circle cx="6" cy="4" r="1.6" fill="#fff"/></svg></span><span class="act edit"><svg width="8" height="8"><use href="#pencil"/></svg></span></div>
      </div>
      <div class="row"><span class="cell" style="width:118px"><span class="avatar" style="background:#3a2e2a" role="img" aria-label="Staff photo"></span>Miles Brandt</span><span class="cell" style="width:80px">Teacher's Aide</span><span class="cell" style="width:118px"><span class="avatar" style="background:#4d4648" role="img" aria-label="Substitute photo"></span>Rafael Duquette</span><span class="cell" style="width:67px"><span class="pill approved">APPROVED</span></span><span class="time"><span class="date">02/03 - 02/07</span><span class="dur"><svg width="7" height="7"><use href="#clock"/></svg>3h 45m</span></span></div>
      <div class="row"><span class="cell" style="width:118px"><span class="avatar" style="background:#7a7880" role="img" aria-label="Staff photo"></span>Gwen Talbot</span><span class="cell" style="width:80px">Food service</span><span class="cell" style="width:118px"><span class="avatar" style="background:#9b6a5c" role="img" aria-label="Substitute photo"></span>Iris Callow</span><span class="cell" style="width:67px"><span class="pill cancelled">CANCELLED</span></span><span class="time"><span class="date">12/30 - 01/01</span><span class="dur"><svg width="7" height="7"><use href="#clock"/></svg>2h 30m</span></span></div>
      <div class="row"><span class="cell" style="width:118px"><span class="avatar" style="background:#d9b48a" role="img" aria-label="Staff photo"></span>Nora Whitfield</span><span class="cell" style="width:80px">Teacher</span><span class="cell" style="width:118px"><span class="avatar" style="background:#c9a884" role="img" aria-label="Substitute photo"></span>Paula Renwick</span><span class="cell" style="width:67px"><span class="pill approved">APPROVED</span></span><span class="time"><span class="date">02/12 - 02/16</span><span class="dur"><svg width="7" height="7"><use href="#clock"/></svg>4h 30m</span></span></div>
      <span class="scroll" style="left:496px;top:70px;height:44px"></span>
    </section>

    <!-- Monthly fill rate -->
    <section class="card" style="top:82px;height:199px">
      <svg class="abs" style="left:10px;top:12px" width="12" height="12" viewBox="0 0 12 12"><circle cx="6" cy="6" r="5.5" fill="#c9c5d8"/><path d="M6 .5V6h5.5A5.5 5.5 0 006 .5z" fill="#6a50bd"/></svg>
      <h3 style="top:10px">Monthly fill rate</h3>
      <svg class="abs" style="left:53px;top:34px" width="82" height="82" viewBox="0 0 82 82">
        <g transform="rotate(-90 41 41)" fill="none" stroke-width="9">
          <circle cx="41" cy="41" r="36" stroke="#6a50bd" stroke-dasharray="124 226.2"/>
          <circle cx="41" cy="41" r="36" stroke="#4e7ee0" stroke-dasharray="34 226.2" stroke-dashoffset="-124"/>
          <circle cx="41" cy="41" r="36" stroke="#2bb3d6" stroke-dasharray="68.2 226.2" stroke-dashoffset="-158"/>
        </g>
        <text x="41" y="42" text-anchor="middle" font-family="Poppins,sans-serif" font-size="12.5" font-weight="600" fill="#1c1a28">45</text>
        <text x="41" y="52" text-anchor="middle" font-family="Poppins,sans-serif" font-size="6" fill="#8a8799">Total Jobs</text>
      </svg>
      <div class="legend-row" style="top:126px">Open<span class="bar"><i style="width:45%;background:#6a50bd"></i></span><span class="v">20 <span>jobs</span></span><span class="p">45%</span></div>
      <div class="legend-row" style="top:150px">Filled<span class="bar"><i style="width:28%;background:#4e7ee0"></i></span><span class="v">16 <span>jobs</span></span><span class="p">35%</span></div>
      <div class="legend-row" style="top:174px">No Sub<span class="bar"><i style="width:16%;background:#2bb3d6"></i></span><span class="v">9 <span>jobs</span></span><span class="p">20%</span></div>
    </section>

    <!-- Pending profile images -->
    <section class="card" style="top:294px;height:320px">
      <svg class="abs" style="left:10px;top:13px" width="12" height="11" viewBox="0 0 12 11"><path d="M6 .5L11.5 10.5H.5z" fill="#8c86a8"/><path d="M6 4v3" stroke="#fff" stroke-width="1.1"/><circle cx="6" cy="8.6" r=".7" fill="#fff"/></svg>
      <h3 style="top:11px">Pending Profile Images</h3>
      <div class="profile" style="top:47px"><span class="sep"></span><span class="face" style="background:linear-gradient(135deg,#7a4a35,#3a2620)" role="img" aria-label="Submitted profile photo"></span><span class="nm">Maren Ashby</span><span class="vf">None-verified</span><span class="btn approve"><svg width="6" height="6"><use href="#check-badge"/></svg>Approve</span><span class="btn decline"><svg width="6" height="6"><use href="#ban"/></svg>Decline</span></div>
      <div class="profile" style="top:100px"><span class="sep"></span><span class="face" style="background:linear-gradient(135deg,#b08468,#4b3a33)" role="img" aria-label="Submitted profile photo"></span><span class="nm">Calvin Roost</span><span class="vf"><svg width="6" height="6"><use href="#check-badge"/></svg>Verified</span><span class="btn approve"><svg width="6" height="6"><use href="#check-badge"/></svg>Approve</span><span class="btn decline"><svg width="6" height="6"><use href="#ban"/></svg>Decline</span></div>
      <div class="profile" style="top:151px"><span class="sep"></span><span class="face" style="background:linear-gradient(135deg,#8b8b8b,#2a2a2a)" role="img" aria-label="Submitted profile photo"></span><span class="nm">Ethan Vargo</span><span class="vf">None-verified</span><span class="btn approve"><svg width="6" height="6"><use href="#check-badge"/></svg>Approve</span><span class="btn decline"><svg width="6" height="6"><use href="#ban"/></svg>Decline</span></div>
      <div class="profile" style="top:202px"><span class="sep"></span><span class="face" style="background:linear-gradient(135deg,#c8603a,#e8c0a4)" role="img" aria-label="Submitted profile photo"></span><span class="nm">Lucia Fenn</span><span class="vf">None-verified</span><span class="btn approve"><svg width="6" height="6"><use href="#check-badge"/></svg>Approve</span><span class="btn decline"><svg width="6" height="6"><use href="#ban"/></svg>Decline</span></div>
      <div class="profile" style="top:256px"><span class="sep"></span><span class="face" style="background:linear-gradient(135deg,#b0604e,#4a2a26)" role="img" aria-label="Submitted profile photo"></span><span class="nm">Owen Dray</span><span class="vf"><svg width="6" height="6"><use href="#check-badge"/></svg>Verified</span><span class="btn approve"><svg width="6" height="6"><use href="#check-badge"/></svg>Approve</span><span class="btn decline"><svg width="6" height="6"><use href="#ban"/></svg>Decline</span></div>
    </section>
  </main>
</div>

<svg class="connectors" viewBox="0 0 1200 870">
  <g stroke="#2bb3d6" stroke-width="1" fill="none">
    <path d="M496 412V769H424"/>
    <path d="M705 615V769H778"/>
  </g>
  <circle cx="496" cy="412" r="3" fill="#2bb3d6"/>
  <circle cx="705" cy="615" r="3" fill="#2bb3d6"/>
  <path d="M421 769l5-3v6z" fill="#2bb3d6"/>
  <path d="M782 769l-5-3v6z" fill="#2bb3d6"/>
</svg>

<p class="annot" style="left:78px"><span class="tag">Edit</span>and<span class="tag">Delete</span>action buttons will appear when hovering a table row</p>
<p class="annot" style="left:789px"><span class="tag">Edit</span>and<span class="tag">View</span>action buttons will appear when hovering a table row</p>
</body>
</html>
```